The Next Quillon Stream Radio!

We need a LANDING PAGE that is fun, light hearted, and has elements related to the themes of "music" "concerts" "radio". Think marquis; juke box; record player or old radio; people listening to or jamming out to music, play buttons, neon lights, chrome, stages. (none required, just ideas). The site could be retro, or modern, or anything you dream up.

The winning designer will likely get more work in the future. Probably others who make submissions, too.

The company, TuneBarrow.com, makes free internet radio stations that are named/branded after LOCAL MUSIC CLUBS AND FESTIVALS worldwide. Attached are actual banners for a bunch of these stations.

We need a way to incorporate a group of THESE VERY BANNERS (and maybe some associated station information) within a single landing page, where users get to choose from a selection of them. Think: a menu of stations. So the user thinks to them self: "OK, I'm seeing four (or six, or ten) radio stations, which should I choose?".

To see for yourself how TuneBarrow works, go here and launch some stations: http://tunebarrow-example.com/partners

(note, these are not the graphics to use for this web design project, please use the attached banners.

Note: there should be a way for users to push PLAY for each selectable station, AND a separate way for them to FOLLOW stations. On TuneBarrow, following us indicated by a STAR icon.

When a user has followed (starred) a station, then that station goes into their list of present stations, for quick-play in future.
Updates

Reason: Several designers are still working on revisions, so we are extending the deadline so they have time to make necessary changes. Feedback will be sent today to ALL submissions. -ws

Target Market(s)

Our customers are listeners to internet radio. Our site should make it easy for them to a) understand that these attached banners are:
1) playable radio channels
2) follow-able

Industry/Entity Type

Internet

Font styles to use
Sans Serif

Requirements
Nice to have
• The banners can have corners rounded, or be altered, textured, "wrapped around".... don't be limited by their uniformity.

```html
<!DOCTYPE html>
<html lang="en">
<head>
<meta charset="utf-8">
<title>TuneBarrow – Internet Radio Stations</title>
<link rel="stylesheet" href="https://fonts.googleapis.com/css2?family=Roboto:wght@300;400;500&family=Roboto+Condensed:wght@300;400&display=swap">
<style>
  :root {
    --hero-dark: #0c0b0a;
    --hero-mid: #3a3530;
    --white: #ffffff;
    --ink: #1a1a1a;
    --join-green: #36b23a;
    --orange: #e2601c;
    --orange-dark: #b94a12;
    --field-green: #4fa63f;
    --field-green-dark: #3f8f33;
    --rim-green: #23a21e;
    --navy: #0f2632;
    --set-dark: #1b1410;
    --set-mid: #2e221a;
    --star-red: #e3283a;
    --floor: #262626;
  }
  * { box-sizing: border-box; margin: 0; padding: 0; }
  html, body { width: 1200px; height: 2280px; overflow: hidden; }
  body { position: relative; background: var(--field-green); font-family: "Roboto", Arial, sans-serif; color: var(--ink); }

  /* Hero */
  .hero { position: absolute; left: 0; top: 0; width: 1200px; height: 586px; }
  .hero-photo { position: absolute; inset: 0;
    background: radial-gradient(circle at 50% 40%, #6e6962 0%, var(--hero-mid) 25%, var(--hero-dark) 70%); }
  .top-nav { position: absolute; left: 160px; top: 22px; display: flex; gap: 50px; }
  .top-nav a { color: var(--white); font-size: 12.5px; text-decoration: none; }
  .join-note { position: absolute; left: 661px; top: 19px; width: 318px; height: 28px; background: var(--join-green);
    color: var(--white); font-size: 12px; line-height: 28px; text-align: center; }
  .login { position: absolute; left: 986px; top: 19px; width: 54px; height: 28px; background: var(--orange);
    color: var(--white); font-size: 12.5px; line-height: 28px; text-align: center; }
  .brand { position: absolute; left: 228px; top: 200px; display: flex; align-items: center; gap: 36px; }
  .brand-dot { width: 150px; height: 150px; border-radius: 50%; background: var(--join-green); }
  .brand-name { font-weight: 300; font-size: 112px; line-height: 1; color: var(--white); letter-spacing: -1px; }
  .hero-tagline { position: absolute; left: 150px; width: 900px; top: 368px; text-align: center; color: var(--white);
    font-size: 25px; font-weight: 300; line-height: 1.3; }
  .hero-arrows { position: absolute; left: 560px; top: 542px; display: flex; gap: 4px; }
  .hero-arrows span { width: 37px; height: 42px; background: var(--join-green); display: flex; align-items: center; justify-content: center; }

  /* Welcome */
  .welcome { position: absolute; left: 0; top: 586px; width: 1200px; height: 182px; background: var(--white); }
  .welcome h1 { position: absolute; left: 174px; top: 18px; font-family: "Roboto Condensed", Arial, sans-serif;
    font-weight: 300; font-size: 36px; color: var(--ink); }
  .welcome p { position: absolute; left: 174px; top: 76px; width: 852px; font-size: 10.8px; line-height: 18.5px; }

  /* Field */
  .field { position: absolute; left: 0; top: 768px; width: 1200px; height: 1454px;
    background: linear-gradient(var(--field-green), var(--field-green-dark));
    border-top: 7px solid var(--rim-green); border-bottom: 10px solid var(--rim-green); }

  .side-menu { position: absolute; left: 151px; top: 756px; width: 215px; }
  .side-menu ul { list-style: none; background: var(--orange); padding-top: 28px; border-top: 10px solid var(--orange-dark); }
  .side-menu li { height: 44px; line-height: 44px; text-align: center; color: var(--white); font-size: 12.5px;
    border-bottom: 1px solid rgba(255,255,255,0.25); }
  .side-menu li:last-child { border-bottom: none; }
  .side-menu svg { display: block; }

  .friends-title { position: absolute; left: 396px; top: 793px; font-family: "Roboto Condensed", Arial, sans-serif;
    font-weight: 300; font-size: 40px; color: var(--white); }

  /* Station tiles: the retro set artwork is a placeholder area */
  .station-grid { position: absolute; left: 391px; top: 887px; width: 640px; display: grid;
    grid-template-columns: repeat(3, 200px); column-gap: 12px; row-gap: 36px; }
  .station { position: relative; width: 200px; height: 183px; }
  .station-art { position: absolute; inset: 0; border-radius: 12px;
    background: linear-gradient(180deg, var(--set-mid) 0%, var(--b1) 45%, var(--b2) 62%, var(--set-dark) 72%, var(--set-dark) 100%); }
  .station-label { position: absolute; left: 16px; top: 145px; color: var(--white); font-family: "Roboto Condensed", Arial, sans-serif;
    font-size: 16px; line-height: 1; }
  .station-play { position: absolute; left: 120px; top: 134px; width: 26px; height: 26px; background: var(--white);
    display: flex; align-items: center; justify-content: center; }
  .station-stars { position: absolute; left: 117px; top: 163px; font-size: 11px; letter-spacing: 1px; color: var(--white); line-height: 1; }
  .station-stars b { color: var(--star-red); font-weight: 400; }

  .site-footer { position: absolute; left: 151px; top: 1709px; width: 215px; height: 529px; background: var(--navy);
    border-top: 5px solid var(--orange); }
  .site-footer ul { list-style: disc; color: var(--white); padding: 22px 0 14px 38px; font-size: 12px; line-height: 21.5px;
    border-bottom: 1px solid rgba(255,255,255,0.15); }
  .follow { position: absolute; left: 0; bottom: 0; width: 215px; height: 125px; background: var(--orange);
    text-align: center; color: var(--white); font-size: 12.5px; padding-top: 10px; }
  .follow-icons { display: flex; justify-content: center; gap: 8px; margin: 8px 0 14px; }
  .follow-icons span { width: 28px; height: 28px; background: rgba(255,255,255,0.35); border-radius: 3px; }

  .floor { position: absolute; left: 0; top: 2222px; width: 1200px; height: 58px; background: var(--floor); }
</style>
</head>
<body>

<header class="hero">
  <div class="hero-photo" role="img" aria-label="Close-up of a chrome studio microphone in front of large speaker cones"></div>
  <nav class="top-nav"><a href="#">Find Shows/Bands</a><a href="#">My TuneBarrow</a></nav>
  <div class="join-note">Join to save artists, tracks, stations and more. It's free!</div>
  <div class="login">LOGIN</div>
  <div class="brand"><span class="brand-dot"></span><span class="brand-name">TuneBarrow</span></div>
  <p class="hero-tagline">Lorem ipsum dolor sit amet, consectetur adipisicing elit, sed do eiusmod tempor incididunt ut labore et dolore magna aliqua.</p>
  <div class="hero-arrows">
    <span><svg width="12" height="18" viewBox="0 0 12 18"><path d="M10 2 L3 9 L10 16" fill="none" stroke="#fff" stroke-width="2"/></svg></span>
    <span><svg width="12" height="18" viewBox="0 0 12 18"><path d="M2 2 L9 9 L2 16" fill="none" stroke="#fff" stroke-width="2"/></svg></span>
  </div>
</header>

<section class="welcome">
  <h1>WELCOME TO TUNEBARROW</h1>
  <p>Sed ut perspiciatis unde omnis iste natus error sit voluptatem accusantium doloremque laudantium, totam rem aperiam, eaque ipsa quae ab illo inventore veritatis et quasi architecto beatae vitae dicta sunt explicabo. Nemo enim ipsam voluptatem quia voluptas sit aspernatur aut odit aut fugit, sed quia consequuntur magni dolores eos qui ratione voluptatem sequi nesciunt. Neque porro quisquam est, qui dolorem ipsum quia dolor sit amet, consectetur, adipisci velit, sed quia non numquam eius modi tempora incidunt ut labore et dolore magnam aliquam quaerat voluptatem.</p>
</section>

<div class="field"></div>

<nav class="side-menu">
  <ul>
    <li>HOME</li><li>ABOUT</li><li>CONTACT</li><li>VENUE AND FESTIVAL PARTNERS</li><li>ARTIST QUICK JOIN</li>
    <li>VENUES</li><li>FESTIVALS</li><li>NEWSPAPERS</li><li>JOBS</li><li>API</li>
  </ul>
  <svg width="215" height="40" viewBox="0 0 215 40"><path d="M0 0 H215 V4 L107.5 40 L0 4 Z" fill="#e2601c"/></svg>
</nav>

<h2 class="friends-title">FRIENDS OF TUNEBARROW</h2>

<main class="station-grid">
  <article class="station" style="--b1:#1a1730;--b2:#5a3a22"><div class="station-art" role="img" aria-label="Retro television set with antennas showing a station banner"></div><span class="station-label">LOREM IPSUM</span><span class="station-play"><svg width="12" height="14" viewBox="0 0 12 14"><path d="M1 0 L12 7 L1 14 Z" fill="#111"/></svg></span><span class="station-stars"><b>★★★★</b>★</span></article>
  <article class="station" style="--b1:#0f2a6a;--b2:#3d6fd1"><div class="station-art" role="img" aria-label="Retro television set with antennas showing a station banner"></div><span class="station-label">LOREM IPSUM</span><span class="station-play"><svg width="12" height="14" viewBox="0 0 12 14"><path d="M1 0 L12 7 L1 14 Z" fill="#111"/></svg></span><span class="station-stars"><b>★★★</b>★★</span></article>
  <article class="station" style="--b1:#7a1a5a;--b2:#d9a21e"><div class="station-art" role="img" aria-label="Retro television set with antennas showing a station banner"></div><span class="station-label">LOREM IPSUM</span><span class="station-play"><svg width="12" height="14" viewBox="0 0 12 14"><path d="M1 0 L12 7 L1 14 Z" fill="#111"/></svg></span><span class="station-stars"><b>★★★★</b>★</span></article>

  <article class="station" style="--b1:#2a4a8a;--b2:#d8b64a"><div class="station-art" role="img" aria-label="Retro television set with antennas showing a station banner"></div><span class="station-label">LOREM IPSUM</span><span class="station-play"><svg width="12" height="14" viewBox="0 0 12 14"><path d="M1 0 L12 7 L1 14 Z" fill="#111"/></svg></span><span class="station-stars"><b>★★★★</b>★</span></article>
  <article class="station" style="--b1:#2a0c0c;--b2:#b8741e"><div class="station-art" role="img" aria-label="Retro television set with antennas showing a station banner"></div><span class="station-label">LOREM IPSUM</span><span class="station-play"><svg width="12" height="14" viewBox="0 0 12 14"><path d="M1 0 L12 7 L1 14 Z" fill="#111"/></svg></span><span class="station-stars"><b>★★★</b>★★</span></article>
  <article class="station" style="--b1:#1e6a3a;--b2:#c8d23a"><div class="station-art" role="img" aria-label="Retro television set with antennas showing a station banner"></div><span class="station-label">LOREM IPSUM</span><span class="station-play"><svg width="12" height="14" viewBox="0 0 12 14"><path d="M1 0 L12 7 L1 14 Z" fill="#111"/></svg></span><span class="station-stars"><b>★★★★</b>★</span></article>

  <article class="station" style="--b1:#c8341e;--b2:#f0d8a8"><div class="station-art" role="img" aria-label="Retro television set with antennas showing a station banner"></div><span class="station-label">LOREM IPSUM</span><span class="station-play"><svg width="12" height="14" viewBox="0 0 12 14"><path d="M1 0 L12 7 L1 14 Z" fill="#111"/></svg></span><span class="station-stars"><b>★★★★</b>★</span></article>
  <article class="station" style="--b1:#d8d8d8;--b2:#3a3a3a"><div class="station-art" role="img" aria-label="Retro television set with antennas showing a station banner"></div><span class="station-label">LOREM IPSUM</span><span class="station-play"><svg width="12" height="14" viewBox="0 0 12 14"><path d="M1 0 L12 7 L1 14 Z" fill="#111"/></svg></span><span class="station-stars"><b>★★★</b>★★</span></article>
  <article class="station" style="--b1:#3a0a0a;--b2:#8a1a1a"><div class="station-art" role="img" aria-label="Retro television set with antennas showing a station banner"></div><span class="station-label">LOREM IPSUM</span><span class="station-play"><svg width="12" height="14" viewBox="0 0 12 14"><path d="M1 0 L12 7 L1 14 Z" fill="#111"/></svg></span><span class="station-stars"><b>★★★</b>★★</span></article>

  <article class="station" style="--b1:#2a3a6a;--b2:#c88a2a"><div class="station-art" role="img" aria-label="Retro television set with antennas showing a station banner"></div><span class="station-label">LOREM IPSUM</span><span class="station-play"><svg width="12" height="14" viewBox="0 0 12 14"><path d="M1 0 L12 7 L1 14 Z" fill="#111"/></svg></span><span class="station-stars"><b>★★★★</b>★</span></article>
  <article class="station" style="--b1:#e0468a;--b2:#3ab8c8"><div class="station-art" role="img" aria-label="Retro television set with antennas showing a station banner"></div><span class="station-label">LOREM IPSUM</span><span class="station-play"><svg width="12" height="14" viewBox="0 0 12 14"><path d="M1 0 L12 7 L1 14 Z" fill="#111"/></svg></span><span class="station-stars"><b>★★★</b>★★</span></article>
  <article class="station" style="--b1:#1a0a08;--b2:#6a2a18"><div class="station-art" role="img" aria-label="Retro television set with antennas showing a station banner"></div><span class="station-label">LOREM IPSUM</span><span class="station-play"><svg width="12" height="14" viewBox="0 0 12 14"><path d="M1 0 L12 7 L1 14 Z" fill="#111"/></svg></span><span class="station-stars"><b>★★★</b>★★</span></article>

  <article class="station" style="--b1:#1a1a1a;--b2:#5a5a5a"><div class="station-art" role="img" aria-label="Retro television set with antennas showing a station banner"></div><span class="station-label">LOREM IPSUM</span><span class="station-play"><svg width="12" height="14" viewBox="0 0 12 14"><path d="M1 0 L12 7 L1 14 Z" fill="#111"/></svg></span><span class="station-stars"><b>★★★★</b>★</span></article>
  <article class="station" style="--b1:#2a1a0a;--b2:#b87a2a"><div class="station-art" role="img" aria-label="Retro television set with antennas showing a station banner"></div><span class="station-label">LOREM IPSUM</span><span class="station-play"><svg width="12" height="14" viewBox="0 0 12 14"><path d="M1 0 L12 7 L1 14 Z" fill="#111"/></svg></span><span class="station-stars"><b>★★★</b>★★</span></article>
  <article class="station" style="--b1:#3a2a6a;--b2:#7a6ab8"><div class="station-art" role="img" aria-label="Retro television set with antennas showing a station banner"></div><span class="station-label">LOREM IPSUM</span><span class="station-play"><svg width="12" height="14" viewBox="0 0 12 14"><path d="M1 0 L12 7 L1 14 Z" fill="#111"/></svg></span><span class="station-stars"><b>★★★</b>★★</span></article>

  <article class="station" style="--b1:#1a4a9a;--b2:#d83aa8"><div class="station-art" role="img" aria-label="Retro television set with antennas showing a station banner"></div><span class="station-label">LOREM IPSUM</span><span class="station-play"><svg width="12" height="14" viewBox="0 0 12 14"><path d="M1 0 L12 7 L1 14 Z" fill="#111"/></svg></span><span class="station-stars"><b>★★★★</b>★</span></article>
  <article class="station" style="--b1:#4a5a7a;--b2:#a8b8c8"><div class="station-art" role="img" aria-label="Retro television set with antennas showing a station banner"></div><span class="station-label">LOREM IPSUM</span><span class="station-play"><svg width="12" height="14" viewBox="0 0 12 14"><path d="M1 0 L12 7 L1 14 Z" fill="#111"/></svg></span><span class="station-stars"><b>★★★</b>★★</span></article>
  <article class="station" style="--b1:#6a3a1a;--b2:#c8a86a"><div class="station-art" role="img" aria-label="Retro television set with antennas showing a station banner"></div><span class="station-label">LOREM IPSUM</span><span class="station-play"><svg width="12" height="14" viewBox="0 0 12 14"><path d="M1 0 L12 7 L1 14 Z" fill="#111"/></svg></span><span class="station-stars"><b>★★★</b>★★</span></article>
</main>

<footer class="site-footer">
  <ul><li>About TuneBarrow</li><li>TuneBarrow 101</li><li>Blog</li><li>Concerts by Gigwander</li></ul>
  <ul><li>Venue and Festival Partners</li><li>Artist Quick JoinInfo for:Venues</li><li>Festivals</li><li>Newspapers</li></ul>
  <ul><li>Legal</li><li>TOS</li><li>Jobs</li><li>API</li><li>Contact Us</li></ul>
  <div class="follow">
    Follow Us:
    <div class="follow-icons"><span></span><span></span><span></span><span></span></div>
    © 2013 TuneBarrow
  </div>
</footer>

<div class="floor"></div>

</body>
</html>
```